Bright Orbit IT company Soho london Stationary

We've just had a new logo designed on Pixel Harbor and we now need some Stationary to go with it.
We're a small IT support firm supporting Design companies in Soho London. Most of our clients work on Zorvas and a relatively creative so we want a relatively informal design on our stationary to reflect this.
We'd like to stick with the green in the logo but we're not adverse to adding another few colours to the palette.
Please see the attached file for our logo and not our website.

It Company

```html
<!DOCTYPE html>
<html lang="en">
<head>
<meta charset="utf-8">
<title>Bright Orbit Stationery</title>
<link rel="stylesheet" href="https://fonts.googleapis.com/css2?family=PT+Sans:wght@400;700&family=Cormorant+Garamond:ital@1&display=swap">
<style>
  :root {
    --green: #9ccc13;
    --slate: #6a7066;
    --ink: #2b2b2b;
    --muted: #8a8a8a;
    --paper: #ffffff;
    --faint: #e6e6e6;
    --backdrop: #2e2e2e;
  }
  * { box-sizing: border-box; margin: 0; padding: 0; }
  html, body { width: 1200px; height: 900px; overflow: hidden; }
  body {
    position: relative;
    background: var(--backdrop);
    font-family: "PT Sans", Arial, sans-serif;
    color: var(--ink);
  }
  .sheet {
    position: absolute;
    background: var(--paper);
    overflow: hidden;
    box-shadow: 0 4px 14px rgba(0,0,0,.45);
  }
  .corner, .rise { position: absolute; display: block; }
  .corner { left: 0; top: 0; }
  .rise { right: 0; bottom: 0; transform: rotate(180deg); }
  .brand {
    position: absolute;
    display: flex;
    align-items: center;
    gap: .3em;
    color: var(--green);
    font-weight: 700;
    white-space: nowrap;
    line-height: 1;
  }
  .brand-dot {
    width: .5em; height: .5em;
    border-radius: 50%;
    background: var(--green);
  }
  .address {
    position: absolute;
    font-style: normal;
    line-height: 1.35;
    color: var(--ink);
  }
  .address .phone { color: var(--muted); }
  .web {
    position: absolute;
    font-weight: 700;
    color: var(--slate);
    white-space: nowrap;
  }

  /* Letterhead */
  .letterhead { left: 48px; top: 47px; width: 575px; height: 813px; }
  .letterhead .corner { width: 110px; height: 110px; }
  .letterhead .brand { left: 104px; top: 82px; font-size: 24px; }
  .letterhead .address { left: 385px; top: 73px; font-size: 13px; }
  .letterhead .web { left: 203px; bottom: 22px; font-size: 12px; }
  .letterhead .rise { width: 120px; height: 120px; }

  /* Letter */
  .letter { left: 362px; top: 338px; width: 328px; height: 465px; font-size: 5.8px; line-height: 1.55; }
  .letter .corner { width: 58px; height: 58px; }
  .letter .brand { left: 58px; top: 48px; font-size: 13px; }
  .letter .address { left: 219px; top: 45px; font-size: 6.5px; }
  .letter .date { position: absolute; right: 24px; top: 104px; font-size: 6.5px; }
  .letter .body { position: absolute; left: 60px; top: 126px; width: 244px; }
  .letter .body p { margin-bottom: 8px; }
  .letter .signature { display: block; width: 22px; height: 10px; margin: 12px 0 6px; background: var(--faint); border-radius: 2px; }
  .letter .web { left: 115px; bottom: 11px; font-size: 5.5px; }
  .letter .rise { width: 72px; height: 72px; }

  /* Envelope back */
  .envelope-back { left: 716px; top: 28px; width: 452px; height: 290px; }
  .flap-band {
    position: absolute; left: 0; top: 0; width: 100%; height: 98px;
    background: var(--green);
    border-top-right-radius: 44px;
  }
  .flap-band .web { right: 68px; top: 62px; font-size: 12px; transform: rotate(180deg); }
  .envelope-back .corner { top: 98px; width: 64px; height: 64px; }
  .envelope-back .brand { left: 68px; top: 164px; font-size: 15px; }
  .envelope-back .address { left: 70px; top: 211px; font-size: 8.5px; }

  /* Envelope front */
  .envelope-front { left: 760px; top: 355px; width: 416px; height: 175px; }
  .envelope-front .band { position: absolute; left: 0; top: 0; width: 416px; height: 72px; }
  .envelope-front .web { left: 105px; top: 15px; font-size: 12px; font-weight: 400; letter-spacing: .2px; }

  /* Compliment slip */
  .slip { left: 779px; top: 628px; width: 393px; height: 167px; }
  .slip .corner { width: 56px; height: 56px; }
  .slip .greeting { position: absolute; right: 16px; top: 20px; font-family: "Cormorant Garamond", Georgia, serif; font-style: italic; font-size: 14px; color: var(--slate); }
  .slip .brand { left: 57px; top: 57px; font-size: 13px; }
  .slip .address { left: 57px; top: 90px; font-size: 6.8px; }
  .slip .web { left: 59px; bottom: 11px; font-size: 5.6px; }
  .slip .rise { width: 80px; height: 80px; }
</style>
</head>
<body>

<svg width="0" height="0" style="position:absolute" aria-hidden="true">
  <defs>
    <symbol id="ring-corner" viewBox="0 0 100 100">
      <path d="M0 0 H40 A40 40 0 0 1 0 40 Z" fill="var(--green)"/>
      <path d="M0 58 A58 58 0 0 0 58 0" fill="none" stroke="var(--slate)" stroke-width="6"/>
      <path d="M0 78 A78 78 0 0 0 78 0" fill="none" stroke="var(--green)" stroke-width="8"/>
    </symbol>
  </defs>
</svg>

<section class="sheet letterhead">
  <svg class="corner" aria-hidden="true"><use href="#ring-corner"/></svg>
  <div class="brand"><span class="brand-dot"></span>Bright Orbit</div>
  <address class="address">42 Quill Lane<br>London W1F 8ZQ.<br><span class="phone">Phone : 0207 555 0193</span></address>
  <p class="web">www.bright-orbit.it, info@bright-orbit.it</p>
  <svg class="rise" aria-hidden="true"><use href="#ring-corner"/></svg>
</section>

<section class="sheet letter">
  <svg class="corner" aria-hidden="true"><use href="#ring-corner"/></svg>
  <div class="brand"><span class="brand-dot"></span>Bright Orbit</div>
  <address class="address">42 Quill Lane<br>London W1F 8ZQ.<br><span class="phone">Phone : 0207 555 0193</span></address>
  <p class="date">Date: 16.07.2011</p>
  <div class="body">
    <p>Hello There,</p>
    <p>Thank you for choosing us to look after your studio systems. This letter confirms the support plan we agreed last week, covering your workstations, servers, backups and network, with a named engineer on call during office hours and quick remote help whenever a machine lets you down in the middle of a deadline.</p>
    <p>Your team can reach us by phone or email at any time. Every request is logged, given a reference and followed until it is closed. Each month we will send a short report listing the work done, the updates installed and any hardware that is nearing the end of its life, so you can plan ahead.</p>
    <p>If anything in this plan needs changing, simply let us know and we will update it together. We look forward to working with your studio and keeping every screen running smoothly.</p>
    <p>Best Regards,</p>
    <span class="signature" role="img" aria-label="Handwritten signature"></span>
    <p>Nettleway<br>support@nettleway.co.uk</p>
  </div>
  <p class="web">www.bright-orbit.it, info@bright-orbit.it</p>
  <svg class="rise" aria-hidden="true"><use href="#ring-corner"/></svg>
</section>

<section class="sheet envelope-back">
  <div class="flap-band"><p class="web">www.bright-orbit.it, info@bright-orbit.it</p></div>
  <svg class="corner" aria-hidden="true"><use href="#ring-corner"/></svg>
  <div class="brand"><span class="brand-dot"></span>Bright Orbit</div>
  <address class="address">42 Quill Lane<br>London W1F 8ZQ.<br><span class="phone">Phone : 0207 555 0193</span></address>
</section>

<section class="sheet envelope-front">
  <svg class="band" viewBox="0 0 416 72" preserveAspectRatio="none" aria-hidden="true">
    <path d="M0 0 H416 V72 C300 58 120 44 22 40 Q0 38 0 18 Z" fill="var(--green)"/>
  </svg>
  <p class="web">www.bright-orbit.it, info@bright-orbit.it</p>
</section>

<section class="sheet slip">
  <svg class="corner" aria-hidden="true"><use href="#ring-corner"/></svg>
  <p class="greeting">With Compliment</p>
  <div class="brand"><span class="brand-dot"></span>Bright Orbit</div>
  <address class="address">42 Quill Lane<br>London W1F 8ZQ.<br><span class="phone">Phone : 0207 555 0193</span></address>
  <p class="web">www.bright-orbit.it, info@bright-orbit.it</p>
  <svg class="rise" aria-hidden="true"><use href="#ring-corner"/></svg>
</section>

</body>
</html>
```